Real Estate Managemene Company Needs Business Card Design

We have a logo design and just need business cards made now for our business. Please use PDF logo # 3.

Card with Information to be attached shortly.

The card is used for a real estate management company. We will need to add four other employees and their cards.

Industry/Entity Type

Real Estate

Contact Information for Business Card

Tariq Hamdan
President
3187 Thornwick Avenue
Suite C
Larkfield Springs, OH 44152
Phone 630.417.2286
Fax 630.417.2287
Cell 630.473.8062
vantorp@mailbreeze.net

Once design is approved we will have four other employees
Omar Hamdan
Operations Manager

Nadia Hamdan
Administrative Manager

Faz Hamdan
Principal

We would need to take out the cell # 630.473.8062 out for the remaining three cards.

Requirements
Must have
• Please use logo attached

```html
<!DOCTYPE html>
<html lang="en">
<head>
<meta charset="utf-8">
<title>Business Card – Meridian Property Holdings Group</title>
<link rel="stylesheet" href="https://fonts.googleapis.com/css2?family=Open+Sans:ital,wght@0,400;0,700;1,400&display=swap">
<style>
  :root {
    --backdrop: #d6d6d6;
    --card: #ffffff;
    --ink: #1c1c1c;
    --brand-blue: #1f5f9e;
  }
  html, body {
    margin: 0;
    padding: 0;
    width: 1200px;
    height: 1200px;
    overflow: hidden;
    background: var(--backdrop);
    font-family: "Open Sans", Arial, sans-serif;
  }
  .canvas {
    width: 1200px;
    height: 1200px;
    display: flex;
    align-items: center;
    justify-content: center;
  }
  .business-card {
    position: relative;
    width: 1000px;
    height: 572px;
    background: var(--card);
    box-shadow: 0 6px 24px rgba(0,0,0,0.12);
    color: var(--ink);
  }
  .brand-mark {
    position: absolute;
    left: 300px;
    top: 110px;
    display: flex;
    align-items: center;
    gap: 16px;
  }
  .brand-mark .brand-square {
    width: 34px;
    height: 34px;
    background: var(--ink);
    flex: none;
  }
  .brand-mark .brand-name {
    font-weight: 700;
    font-size: 40px;
    letter-spacing: 1px;
    color: var(--ink);
    line-height: 1.1;
  }
  .company-block {
    position: absolute;
    left: 80px;
    top: 230px;
    font-size: 19px;
    line-height: 1.32;
  }
  .company-block .company-name {
    color: var(--brand-blue);
    font-weight: 700;
    margin: 0 0 2px;
  }
  .company-block address {
    font-style: normal;
  }
  .contact-block {
    position: absolute;
    left: 560px;
    top: 360px;
    font-size: 19px;
    line-height: 1.32;
  }
  .contact-block .person-name {
    color: var(--brand-blue);
    font-weight: 700;
    margin: 0;
  }
  .contact-block .person-title {
    color: var(--brand-blue);
    font-style: italic;
    margin: 0 0 4px;
  }
  .contact-block p { margin: 0; }
</style>
</head>
<body>
<main class="canvas">
  <section class="business-card">
    <div class="brand-mark">
      <span class="brand-square"></span>
      <span class="brand-name">MERIDIAN PROPERTY<br>HOLDINGS GROUP</span>
    </div>

    <div class="company-block">
      <p class="company-name">Meridian Property<br>Holdings Group</p>
      <address>
        3187 Thornwick Avenue<br>
        Suite C<br>
        Larkfield Springs, OH 44152<br>
        USA
      </address>
    </div>

    <div class="contact-block">
      <p class="person-name">Tariq Hamdan</p>
      <p class="person-title">President</p>
      <p>Office +1 (555) 417-2286</p>
      <p>Mobile +1 (555) 473-8062</p>
      <p>Fax +1 (555) 417-2287</p>
      <p>vantorp@mailbreeze.net</p>
    </div>
  </section>
</main>
</body>
</html>
```